Large online photo magazine needs redesign

We have previously digitised a historical photographic magazine of around 20,000 printed pages and made it available online. The magazine ran up to the early 1970s, and the content is largely black and white photographs of local events, accompanied by short captions.

Although the content is very rich, the design needs to be revisited so that:
* it is visually appealing
* it is responsive (i.e. works in browsers across all manner of devices)
* is faithful to the nature of the content

There are only a few core page types, and the central one is the article page, an example of which can be seen at:
http://lanternweekly.org.nz/gisborne/issue/KLW81_19600714/t1-body-d4.html

Any design submitted should be based on the treatment of an article page such as the above.

Given the large number of pages on our site, we need a design which can be templated to work for any content in the collection, i.e. we cannot hand-craft our templates to match a given page of content, rather a template must work acceptably well for all content.

The current site, although basic in design, has the advantage that it is quite efficient in the amount of data per page request (around 100k - 200k). While not adverse to web fonts, banner imagery etc, we will carefully consider the benefit gained from any such treatment against the amount of extra data that needs to be downloaded to the client's browser.

For the right design, we are able ourselves to adapt it to a CSS layout.

An example of each core page type is as follows (though for this project we only expect a design for a single page, as itemised above):

http://lanternweekly.org.nz/gisborne/index.html
http://lanternweekly.org.nz/gisborne/about.html
http://lanternweekly.org.nz/gisborne/help.html
http://lanternweekly.org.nz/gisborne/initial/index.html
http://lanternweekly.org.nz/gisborne/search/results?type=section&text=smith&cmdSubmit=Go
http://lanternweekly.org.nz/gisborne/advanced-search/index.html
http://lanternweekly.org.nz/gisborne/issue/KLW81_19600714/t1-front-d1.html
http://lanternweekly.org.nz/gisborne/issue/KLW81_19600714/index.html
http://lanternweekly.org.nz/gisborne/issue/KLW81_19600714/fig-KLW81_19600714_005a.html
http://lanternweekly.org.nz/gisborne/issue/KLW81_19600714/KLW81_19600714_012.html
http://lanternweekly.org.nz/gisborne/issue/KLW81_19600714/thumbnails.html

Target Market(s)

A general browsing audience of all ages, but skewed towards the older generations, and those interested in family / regional history.

The average user will not be particularly web-savy, and the treatment of the content should not detract / distract from the actual content itself.

Industry/Entity Type

Events

Requirements
Must have
• * it is visually appealing
The content should be visually appealing to the audience, which can be defined as a general browsing audience of all ages, but skewed towards the middle and older generations.

* it is responsive (the design can be adapted - by us - to work in browsers across all manner of devices)

The magazine covers (http://lanternweekly.org.nz/gisborne/issues/index.html) offer some possible inspiration for treatment of the material.

```html
<!DOCTYPE html>
<html lang="en">
<head>
<meta charset="utf-8">
<title>No 81 July 14, 1960 – Gisborne Lantern Weekly</title>
<link rel="stylesheet" href="https://fonts.googleapis.com/css2?family=Raleway:wght@300;400;600&family=Open+Sans:wght@400&display=swap">
<style>
:root{
  --red:#cc3a50;
  --ink:#1e1e1e;
  --muted:#8c8c8c;
  --body:#9a9a9a;
  --rule:#dcdcdc;
  --banner:#111;
  --share:#eef2f7;
}
*{box-sizing:border-box;margin:0;padding:0}
html,body{width:879px;height:1200px;overflow:hidden;background:#fff}
body{font-family:"Raleway",sans-serif;color:var(--ink);position:relative}
a{color:inherit;text-decoration:none}

.utility{height:23px;border-bottom:1px solid var(--rule);display:flex;justify-content:space-between;align-items:center;padding:0 66px;font-size:7.5px;color:var(--muted)}
.utility .links span{margin:0 6px}

.masthead{height:80px;position:relative}
.brand{position:absolute;left:66px;top:16px;display:flex;align-items:center;gap:7px;color:var(--red);font-weight:600;font-size:19px;line-height:22px;white-space:nowrap}
.brand .mark{width:10px;height:10px;background:var(--red);flex:none}
.nav{position:absolute;left:270px;top:57px;display:flex;gap:25px;font-size:9px;color:#555}
.nav .active{border-bottom:1px solid var(--red);padding-bottom:2px}
.search{position:absolute;left:621px;top:52px;width:193px;height:18px;border:1px solid var(--rule);font-size:7px;color:#bbb;padding:5px 7px}
.search .btn{position:absolute;right:-1px;top:-1px;width:19px;height:18px;background:var(--red);display:flex;align-items:center;justify-content:center}

.hero{height:166px;background:var(--banner);color:#eee;font-weight:300;font-size:28px;line-height:33px;text-align:center;padding-top:32px}

.issue-band{margin-top:16px;height:29px;background:var(--red);position:relative}
.issue-band .label{position:absolute;left:50%;transform:translateX(-50%);top:0;height:29px;background:#fff;padding:0 28px;font-size:24px;font-weight:600;line-height:30px;white-space:nowrap;letter-spacing:-.5px}
.issue-band .label::before,.issue-band .label::after{content:"";position:absolute;top:0;width:20px;height:29px;background:repeating-linear-gradient(90deg,var(--red) 0 2px,#fff 2px 4px)}
.issue-band .label::before{left:2px}
.issue-band .label::after{right:2px}

.article-nav{position:relative;height:44px;padding:10px 66px;font-size:8.5px;color:#555}
.article-nav span{margin:0 10px;color:#999}
.print{position:absolute;right:66px;top:14px;display:flex;align-items:center;gap:6px}

.story{display:flex;gap:15px;padding:0 66px 30px 64px;border-bottom:1px solid var(--rule);margin-bottom:30px}
.story:first-of-type{margin-top:6px}
.story:last-of-type{margin-right:85px;padding-right:0}
.photo{flex:none;width:146px;background:linear-gradient(160deg,#d8d4c4,#6f6b5f);border:1px solid #e4e0cc}
.story-title{font-family:"Open Sans",sans-serif;font-size:15px;color:var(--red);font-weight:400}
.meta{display:flex;align-items:center;font-size:7.5px;color:#444;margin:6px 0 10px}
.meta .sep{margin:0 8px}
.share{display:inline-flex;align-items:center;margin-left:10px;font-size:6.5px}
.share b{background:var(--share);border:1px solid #c8d2de;padding:1px 5px;font-weight:600;color:#34528a}
.share i{font-style:normal;border:1px solid #ccc;padding:1px 3px;margin-left:2px;color:#777}
.caption{font-size:7.5px;line-height:10.5px;color:var(--body);max-width:585px}

.footer{position:absolute;left:0;right:0;top:1143px;text-align:center;font-size:8px;color:var(--muted)}
.licence{width:52px;height:17px;background:#222;border-radius:2px;margin:0 auto 6px}
</style>
</head>
<body>
<header>
  <div class="utility">
    <div>Lantern Weekly &gt; Issues &gt; KLW81_19600714 &gt; t1-body-d4</div>
    <div class="links">Advanced Search<span>|</span>Help<span>|</span>Report an error</div>
  </div>
  <div class="masthead">
    <a class="brand" href="http://lanternweekly.org.nz/gisborne/index.html"><span class="mark"></span><span>Gisborne<br>Lantern Weekly</span></a>
    <nav class="nav">
      <a class="active" href="http://lanternweekly.org.nz/gisborne/index.html">Home</a>
      <a href="http://lanternweekly.org.nz/gisborne/about.html">About</a>
      <a href="http://lanternweekly.org.nz/gisborne/issues/index.html">Brows Gisborne Lantern Weekly</a>
      <a href="http://lanternweekly.org.nz/gisborne/initial/index.html">A-Z People</a>
    </nav>
    <div class="search">Search Gisborne Lantern Weekly
      <span class="btn"><svg width="9" height="9" viewBox="0 0 10 10"><circle cx="4" cy="4" r="3" fill="none" stroke="#fff" stroke-width="1.3"/><line x1="6.2" y1="6.2" x2="9" y2="9" stroke="#fff" stroke-width="1.3"/></svg></span>
    </div>
  </div>
  <div class="hero">Full-text archive of Gisborne Lantern Weekly,<br>a monthly serial published<br>by Harrow Publishing Company between 1954 and 1975.</div>
</header>

<div class="issue-band"><h1 class="label">No 81 July 14, 1960</h1></div>

<div class="article-nav">
  Previous article<span>|</span>Issue contents<span>|</span>Next article
  <div class="print"><svg width="16" height="15" viewBox="0 0 16 15"><rect x="4" y="0" width="8" height="4" fill="#222"/><rect x="0" y="4" width="16" height="7" rx="1.5" fill="#222"/><rect x="4" y="9" width="8" height="6" fill="#fff" stroke="#222" stroke-width="1.2"/></svg>Print This Artical</div>
</div>

<main>
  <article class="story">
    <div class="photo" style="height:165px" role="img" aria-label="Black and white photograph of three sisters in air hostess uniforms, with printed caption below"></div>
    <div class="story-body">
      <h2 class="story-title">Flying Sisters from Gisborne</h2>
      <div class="meta">Read The Review<span class="sep">|</span>9 Comments<span class="share"><b>Post</b><i>35</i></span><span class="share"><b>Like</b><i>26</i></span></div>
      <p class="caption">This is probably something of a record—three sisters who are all air hostesses. They are the Pellow sisters....Marguerite, Elsa, and Rowena, daughters of Mr and Mrs H. T. Pellow, Kestrel Road, Gisborne.</p>
    </div>
  </article>

  <article class="story">
    <div class="photo" style="height:356px" role="img" aria-label="Black and white photograph of an air hostess stepping down from an aircraft doorway"></div>
    <div class="story-body">
      <h2 class="story-title">Flying Sisters from Gisborne</h2>
      <div class="meta">Read The Review<span class="sep">|</span>9 Comments<span class="share"><b>Post</b><i>35</i></span><span class="share"><b>Like</b><i>26</i></span></div>
      <p class="caption">And this young lady, Doreen Haslett, of Auckland, has made history in another way. She was the first air hostess to make a scheduled flight to Gisborne, on Sunday of last week. Hostess service has been extended by C.A.S. to include Gisborne flights, beginning with the Sunday Services.</p>
    </div>
  </article>

  <article class="story">
    <div class="photo" style="height:83px" role="img" aria-label="Black and white photograph of an old highway bridge across a river, with printed caption below"></div>
    <div class="story-body">
      <h2 class="story-title">BRIDGE IN SPLINTS</h2>
      <div class="meta">Read The Review<span class="sep">|</span>9 Comments<span class="share"><b>Post</b><i>35</i></span><span class="share"><b>Like</b><i>26</i></span></div>
      <p class="caption">The old highway bridge across the Waiapu River near Ruatoria probably has more Bailey "splints" than any other bridge in the country. It is to be replaced soon by a modern structure two miles downstream, after which all main-route traffic will pass through Ruatoria township. (Picture, Eastland)</p>
    </div>
  </article>
</main>

<footer class="footer">
  <div class="licence" role="img" aria-label="Licence badge"></div>
  © Copyright 2003-2014 Frame Ninety Limited
</footer>
</body>
</html>
```